High-end construction company needs a business card design

We need a modern looking business card that draws people in, is memorable and looks so good people will want to sick it on their fridges.
On the first side what is needed are:
Logo
My name - Tomas Brevik
Title - Managing Director
Website - www.kelvora.co.uk
Email - tomas@kelvora.co.uk
Telephone - 020 4917 2365
Mobile - 07845139072
On the back side was is needed is a list of all the services we provide:
-Kitchen Renovations
-Bathroom Renovations
-House Renovations
-Garage Conversions
-Extensions
-Loft Conversions
-Conservatories
-Carpentry
-Tiling
-Electrical
-Plumbing & Heating
-Bricklaying
-Landscaping
-Decorating
-Plastering
We would like the colours to be the same shades as on the logo with grey or black for the words.
Target Market(s)
Anyone who needs building work done
Contact Information for Business Card
This business card is for a construction company which strives to deliver excellent service and quality.
The look and feel of the card should represent this.
Requirements
Must have
- On the first side what is needed are:
Logo
My name - Tomas Brevik
Title - Managing Director
Website - www.kelvora.co.uk
Email - tomas@kelvora.co.uk
Telephone - 020 4917 2365
Mobile - 07845139072
Nice to have
- Cool looking features

```html
<!DOCTYPE html>
<html lang="en">
<head>
<meta charset="utf-8">
<title>Kelvora Construction – Business Card</title>
<link href="https://fonts.googleapis.com/css2?family=Arimo:wght@400;700&display=swap" rel="stylesheet">
<style>
  :root {
    --green: #72bd42;
    --green-dark: #3f8a3c;
    --green-mid: #a9d68a;
    --green-pale: #eef7e7;
    --ink: #333333;
    --rule: #9a9a9a;
    --card: #ffffff;
    --backdrop: #d9d9d9;
  }
  * { margin: 0; padding: 0; box-sizing: border-box; }
  html, body {
    width: 1200px; height: 1200px; overflow: hidden;
    background: var(--backdrop);
    font-family: "Arimo", Arial, sans-serif;
  }
  .card {
    position: absolute;
    top: 303px;
    width: 368px; height: 594px;
    background: var(--card);
    border-radius: 12px;
    overflow: hidden;
  }
  .card--services { left: 200px; }
  .card--contact { left: 600px; }

  /* services side */
  .hero-art {
    position: absolute; left: 0; top: 0; width: 100%; height: 254px;
    background: linear-gradient(145deg, var(--green-pale) 0%, var(--green-mid) 55%, var(--green-dark) 100%);
  }
  .service-band {
    position: absolute; left: 0; top: 254px; width: 100%; height: 340px;
    background: var(--green);
  }
  .service-list {
    list-style: none;
    position: absolute; left: 0; right: 0; top: 54px;
    text-align: center; color: #fff;
    font-size: 17px; line-height: 21.8px; letter-spacing: 0.1px;
  }
  .service-list li:nth-child(7) { margin-top: 4px; }

  /* contact side */
  .brand {
    position: absolute; left: 0; right: 0; top: 178px;
    text-align: center;
    color: var(--green);
    font-weight: 700;
    white-space: nowrap;
  }
  .brand__name {
    display: block;
    font-size: 50px; line-height: 58px; letter-spacing: 1px;
  }
  .brand__mark {
    display: inline-block; width: 12px; height: 12px;
    background: var(--green); vertical-align: middle; margin-right: 8px;
    position: relative; top: -4px;
  }
  .brand__sub {
    display: block;
    font-size: 15px; line-height: 18px; letter-spacing: 5px;
    margin-top: 2px;
  }
  .person {
    position: absolute; left: 0; right: 0; top: 364px; text-align: center;
  }
  .person__name {
    color: var(--green); font-weight: 700; font-size: 24px; letter-spacing: 0.3px;
  }
  .person__title {
    color: var(--green-dark); font-size: 15px; margin-top: 3px; letter-spacing: 0.3px;
  }
  .icon-row {
    position: absolute; left: 0; right: 0; top: 428px;
    display: flex; justify-content: center; align-items: center; gap: 4px;
  }
  .icon-row__rule { width: 36px; height: 1px; background: var(--rule); margin: 0 3px; }
  .icon {
    width: 26px; height: 26px; border-radius: 4px; background: var(--green);
    display: flex; align-items: center; justify-content: center;
  }
  .contact-lines {
    position: absolute; left: 0; right: 0; top: 466px;
    text-align: center; color: var(--ink);
    font-size: 17px; line-height: 21.7px;
  }
  .contact-lines .web { color: var(--green-dark); }
</style>
</head>
<body>

<section class="card card--services">
  <div class="hero-art" role="img" aria-label="Illustration of an excavator arm reaching over a house and city buildings"></div>
  <div class="service-band">
    <ul class="service-list">
      <li>KITCHEN RENOVATIONS</li>
      <li>BATHROOM RENOVATIONS</li>
      <li>EXTENSIONS | LOFT CONVERSIONS</li>
      <li>CONSERVATORIES &nbsp;| CARPENTRY</li>
      <li>HOUSE RENOVATIONS</li>
      <li>GARAGE CONVERSIONS</li>
      <li>TILING | ELECTRICAL</li>
      <li>PLUMBING &amp; HEATING</li>
      <li>BRICKLAYING | LANDSCAPING</li>
      <li>DECORATING | PLASTERING</li>
    </ul>
  </div>
</section>

<section class="card card--contact">
  <div class="brand">
    <span class="brand__name"><span class="brand__mark"></span>KELVORA</span>
    <span class="brand__sub">CONSTRUCTION LTD</span>
  </div>

  <div class="person">
    <div class="person__name">TOMAS BREVIK</div>
    <div class="person__title">MANAGING DIRECTOR</div>
  </div>

  <div class="icon-row">
    <span class="icon-row__rule"></span>
    <span class="icon" aria-label="Telephone">
      <svg width="16" height="14" viewBox="0 0 16 14"><path d="M1 5 Q8 -1 15 5 L13 7 L11 5.5 L11 4 Q8 3 5 4 L5 5.5 L3 7 Z" fill="#fff"/><rect x="3" y="8" width="10" height="5" rx="1" fill="#fff"/></svg>
    </span>
    <span class="icon" aria-label="Mobile">
      <svg width="12" height="18" viewBox="0 0 12 18"><rect x="1" y="1" width="10" height="16" rx="2" fill="none" stroke="#fff" stroke-width="1.6"/><circle cx="6" cy="14.3" r="1" fill="#fff"/></svg>
    </span>
    <span class="icon" aria-label="Email">
      <svg width="18" height="13" viewBox="0 0 18 13"><rect x="1" y="1" width="16" height="11" fill="none" stroke="#fff" stroke-width="1.4"/><path d="M1 1 L9 7.5 L17 1 M1 12 L7 6 M17 12 L11 6" fill="none" stroke="#fff" stroke-width="1.2"/></svg>
    </span>
    <span class="icon" aria-label="Website">
      <svg width="16" height="16" viewBox="0 0 16 16"><circle cx="8" cy="8" r="7" fill="#fff"/><path d="M4 4 Q7 5 6 8 Q5 10 7 12 M10 3 Q9 6 12 7" fill="none" stroke="#72bd42" stroke-width="1.6"/></svg>
    </span>
    <span class="icon-row__rule"></span>
  </div>

  <div class="contact-lines">
    <div>020 4917 2365</div>
    <div>07845139072</div>
    <div>tomas@kelvora.co.uk</div>
    <div class="web">www.kelvora.co.uk</div>
  </div>
</section>

</body>
</html>
```